Web Design Project - Event Management Company

A web-page design needs to be created for an event management company. The logo has already been created, the design needs to draw on the themes and colors of the logo and extend on that.

The event management company likes to differentiate itself from others by being a bit "un-conventional" and being able to think outside the box.

the specialise in corporate events, weddings, AGMs, anything that requires coordination of resources. They also can provide Audio Visual services such as recording events.

final design will also require HTML implementation

```html
<!DOCTYPE html>
<html lang="en">
<head>
<meta charset="utf-8">
<title>Odd Tile Group – Creative Events &amp; Party Planners</title>
<link rel="stylesheet" href="https://fonts.googleapis.com/css2?family=Open+Sans:wght@300;400;600&display=swap">
<style>
  :root {
    --white: #ffffff;
    --black: #000000;
    --ink: #333333;
    --muted: #9a9a9a;
    --lime: #c8cc1c;
    --sky: #6cc3e4;
    --amber: #f2a23a;
    --orange: #ef7d1a;
    --icon-grey: #5a5a5a;
    --magenta: #8a1a5a;
    --teal: #1c7a6a;
  }
  * { margin: 0; padding: 0; box-sizing: border-box; }
  html, body { width: 1200px; height: 714px; overflow: hidden; }
  body {
    position: relative;
    font-family: "Open Sans", sans-serif;
    background: var(--black);
  }
  .backdrop {
    position: absolute; inset: 0;
    background:
      radial-gradient(ellipse 160px 90px at 60px 290px, rgba(138,26,90,.55), transparent 70%),
      radial-gradient(ellipse 120px 200px at 1130px 350px, rgba(28,122,106,.5), transparent 70%),
      linear-gradient(var(--white) 0 126px, var(--black) 126px);
  }
  .backdrop-top {
    position: absolute; left: 480px; top: 0; width: 720px; height: 126px;
    background:
      radial-gradient(ellipse 160px 80px at 120px 100px, rgba(242,230,120,.25), transparent 70%),
      radial-gradient(ellipse 220px 90px at 540px 20px, rgba(108,195,228,.2), transparent 70%);
  }
  .site-header { position: absolute; left: 0; top: 0; width: 1200px; height: 97px; }
  .brand {
    position: absolute; left: 165px; top: 58px;
    display: flex; align-items: center; gap: 7px;
    font-size: 14px; font-weight: 600; letter-spacing: .3px; color: var(--ink);
  }
  .brand-mark { width: 12px; height: 12px; background: var(--orange); }
  .call {
    position: absolute; right: 159px; top: 32px;
    display: flex; align-items: center; gap: 6px; color: var(--ink);
  }
  .call-label { font-size: 11px; }
  .call-number { font-size: 17px; margin-right: 12px; }
  .social { display: flex; gap: 5px; }
  .social span { width: 19px; height: 19px; border-radius: 50%; background: var(--icon-grey); }
  .social span.active { background: var(--amber); }
  .main-nav {
    position: absolute; right: 160px; top: 72px;
    display: flex; gap: 23px; list-style: none;
    font-size: 13px; color: var(--ink);
  }
  .hero-frame {
    position: absolute; left: 157px; top: 97px; width: 886px; height: 558px;
    background: var(--white);
  }
  .hero {
    position: absolute; left: 162px; top: 104px; width: 876px; height: 410px;
    background:
      radial-gradient(ellipse 220px 160px at 620px 230px, rgba(40,200,210,.55), transparent 70%),
      radial-gradient(ellipse 120px 220px at 370px 130px, rgba(230,120,20,.75), transparent 70%),
      radial-gradient(ellipse 110px 240px at 860px 150px, rgba(230,120,20,.7), transparent 70%),
      linear-gradient(160deg, #1a1410 0%, #0b1a1c 60%, #020404 100%);
  }
  .hero-copy { position: absolute; left: 25px; top: 178px; color: var(--white); }
  .hero-title { font-weight: 300; font-size: 43px; line-height: 42px; }
  .hero-title .lime { color: var(--lime); }
  .hero-title .sky { color: var(--sky); }
  .hero-title .amber { color: var(--amber); }
  .hero-text { margin-top: 12px; font-size: 12.5px; line-height: 19px; width: 300px; }
  .slider-dots { position: absolute; right: 12px; bottom: 16px; display: flex; gap: 7px; }
  .slider-dots span { width: 10px; height: 10px; background: var(--white); }
  .slider-dots span.current { background: var(--orange); }
  .event-tile { position: absolute; top: 523px; height: 129px; }
  .event-tile .label {
    position: absolute; left: 14px; bottom: 16px;
    font-size: 18px; line-height: 18px; color: var(--white); text-transform: uppercase;
  }
  .tile-personal { left: 162px; width: 285px;
    background: radial-gradient(ellipse 90px 60px at 190px 50px, rgba(250,200,80,.8), transparent 70%), #1a1206; }
  .tile-corporate { left: 456px; width: 287px;
    background: radial-gradient(ellipse 140px 80px at 160px 70px, rgba(120,60,160,.7), transparent 75%), #14107a; }
  .tile-wedding { left: 752px; width: 285px;
    background: radial-gradient(ellipse 120px 70px at 160px 60px, rgba(230,60,90,.8), transparent 75%), #2a0810; }
  .site-footer {
    position: absolute; left: 157px; top: 670px; width: 886px;
    display: flex; justify-content: space-between;
    font-size: 9.5px; color: var(--muted);
  }
  .footer-links { display: flex; gap: 8px; list-style: none; }
</style>
</head>
<body>
  <div class="backdrop" role="img" aria-label="Soft flowing colour waves in magenta and teal"></div>
  <div class="backdrop-top"></div>

  <header class="site-header">
    <div class="brand"><span class="brand-mark"></span>ODD TILE GROUP</div>
    <div class="call">
      <span class="call-label">Call Us Now!</span>
      <span class="call-number">0800 - 555 0142</span>
      <div class="social" aria-label="Social links">
        <span></span><span class="active"></span><span></span><span></span><span></span>
      </div>
    </div>
    <ul class="main-nav">
      <li>HOME</li><li>WHAT WE DO</li><li>GALLERY</li><li>ABOUT US</li><li>CONTACT US</li>
    </ul>
  </header>

  <div class="hero-frame"></div>
  <section class="hero" role="img" aria-label="Crowd at a concert hall event under orange and teal stage lights">
    <div class="hero-copy">
      <h1 class="hero-title">CREATIVE<br><span class="lime">EVENTS</span> <span class="sky">&amp;</span> <span class="amber">PARTY</span><br>PLANNERS</h1>
      <p class="hero-text">The standard chunk of Lorem Ipsum used since the 1500s is reproduced below for those interested.</p>
    </div>
    <div class="slider-dots"><span></span><span class="current"></span><span></span><span></span><span></span></div>
  </section>

  <a class="event-tile tile-personal" role="img" aria-label="Candlelit table with champagne glass"><span class="label">Personal<br>Event</span></a>
  <a class="event-tile tile-corporate" role="img" aria-label="Banquet table set for a corporate dinner"><span class="label">Corporate<br>Event</span></a>
  <a class="event-tile tile-wedding" role="img" aria-label="Wedding reception stage in red light"><span class="label">Wedding<br>Event</span></a>

  <footer class="site-footer">
    <ul class="footer-links">
      <li>Party Planners</li><li>|</li><li>Party Organisers</li><li>|</li><li>Event Management</li><li>|</li><li>Wedding Planners</li><li>|</li><li>Testimonials</li>
    </ul>
    <span>© 2012 Bright Kite Events Ltd.</span>
  </footer>
</body>
</html>
```